依頼詳細
下記ブランドコンセプトに沿ったご提案をお願い致します。
プロトタイプを添付いたします。構成等、より優れていると思えるご提案がありましたら無視して頂いて構いません。
ブランドコンセプトは以下の通りです。

-- 以下、ブランドコンセプト
「自然が持つ美しさ」と「暮らす人の思い」を取り入れ『生活が楽しい住まい』を創ります
人々に永く愛されてきた天然素材を使用することで自然素材だけが持つ色や質感から確かな手触りと温もりを暮らす人に与え続けてくれます。新しいだけを追い過ぎず自然素材の持つ機能性を生かして自然の働きでしっかりと家を守る
それは流行に左右されない気品を保つ「素朴で美しい風合い」に仕上がります。

住む人のライフスタイルや好みをしっかりとお聞かせいただいた上で土地を生かし隣地環境と調和のある設計を企画し、その人らしい家を一緒に考えていきます。
それはその人がどんなふうに暮らしていきたいのかを一緒に考え、その地で永く暮らしていくイメージを膨らませ生活が楽しくなる様な空間を提案します。
-- 以上、ブランドコンセプト
サイトURL
http://tovaru.com/
ページ数
1ページ
希望イメージ
シンプル 複雑
単色 カラフル
暗い 明るい
日常 高級
遊び心 厳粛
未来的 伝統的
女性的 男性的
希望する色
納品ファイル
補足説明
トップページに関するプロトタイプを「トップページ.png」として添付しております。
また、素材として利用可能なものは下記dropboxリンクよりご利用ください。
https://www.filoshare-box.net/s/7kq2mz/sample-assets

■ 選んだ理由

全員が色使いやコンテンツの配置などを理由として同デザインを選択しました。
似通ったデザインの中でも全員の目を引く、魅力的な部分があったのだと考えます。

■ 提案者全員のお礼・コメント

今回は多くの皆様に貴重なお時間を使って頂きご提案頂きました事、大変うれしく思い感謝申し上げます。
複数名で選考を行いましたが、選考するメンバー全員でどれも素晴らしいデザインだよねと口をそろえて申しておりました。

本当にありがとうございました。

```html
<!DOCTYPE html>
<html lang="ja">
<head>
<meta charset="utf-8">
<title>Tovaru｜自然素材のナチュラル住宅</title>
<link rel="stylesheet" href="https://fonts.googleapis.com/css2?family=Noto+Sans+JP:wght@400;700&family=Noto+Serif+JP:wght@400;600&display=swap">
<style>
:root{
  --brown:#4b4038;
  --brown-dark:#3a312b;
  --gold:#c8a14c;
  --cream:#f6f3ee;
  --paper:#ffffff;
  --line:#ddd6cc;
  --text:#555049;
  --muted:#8d867d;
  --photo-warm:#d9cbb7;
  --photo-sky:#c9d6df;
}
*{box-sizing:border-box;margin:0;padding:0}
html,body{width:1200px;height:3140px;overflow:hidden}
body{font-family:"Noto Sans JP",sans-serif;color:var(--text);background:var(--cream);font-size:12px;line-height:1.7;position:relative}
.abs{position:absolute}
.topbar{left:0;top:0;width:1200px;height:22px;background:var(--brown);color:#e9e2d8;font-size:10px;line-height:22px;padding-left:40px}
.masthead{left:0;top:22px;width:1200px;height:102px;background:var(--paper)}
.brand{left:48px;top:30px;display:flex;align-items:center;gap:10px}
.brand-mark{width:14px;height:14px;background:var(--gold)}
.brand-name{font-family:"Noto Serif JP",serif;font-size:30px;color:var(--gold);font-weight:600;letter-spacing:2px}
.cta{top:28px;width:210px;height:46px;border:1px solid var(--line);background:var(--paper);display:flex;align-items:center;gap:8px;padding:0 10px;white-space:nowrap}
.cta small{display:block;font-size:9px;color:var(--muted);line-height:1.2}
.cta b{font-size:18px;color:var(--brown);letter-spacing:1px;line-height:1.2}
.cta .mail{font-size:10.5px;color:var(--brown);font-weight:700;line-height:1.3}
.nav{left:40px;top:124px;width:1120px;height:42px;background:var(--paper);border-top:1px solid var(--line);border-bottom:3px solid var(--brown);display:flex}
.nav a{flex:1;text-align:center;line-height:38px;font-size:12px;color:var(--brown);text-decoration:none;border-left:1px solid var(--line)}
.nav a:first-child{border-left:none}
.hero{left:40px;top:178px;width:1120px;height:380px;background:linear-gradient(100deg,#e9e4dc 0%,#f5f1ea 40%,#cfd9e0 75%,#b9a58c 100%)}
.hero-caption{left:40px;top:520px;width:360px;height:38px;background:rgba(60,50,42,.65);color:#fff;font-size:12px;line-height:38px;padding-left:16px}
.panel{background:var(--paper);border:1px solid var(--line)}
.head{display:flex;justify-content:space-between;align-items:baseline;border-bottom:2px solid var(--brown);padding-bottom:4px;margin-bottom:14px}
.head h2{font-family:"Noto Serif JP",serif;font-size:13px;font-weight:600;color:var(--brown);letter-spacing:1px}
.head span{font-size:9px;color:var(--gold)}
.photo{background:linear-gradient(135deg,var(--photo-warm),#efe8dc)}
.photo.sky{background:linear-gradient(160deg,var(--photo-sky),#e7e1d6)}
.copy p{margin-bottom:12px;font-size:11.5px}
.btn{display:block;border:1px solid var(--brown);color:var(--brown);text-align:center;font-size:11px;line-height:30px;height:32px;background:var(--paper);position:relative}
.btn::after{content:"›";position:absolute;right:10px;color:var(--gold)}
.case-grid{display:grid;grid-template-columns:1fr 1fr;gap:10px}
.case-grid div{font-size:9px;color:var(--muted)}
.case-grid .photo{height:88px;margin-bottom:2px}
.news li{list-style:none;display:flex;gap:16px;padding:16px 0;border-bottom:1px dashed var(--line)}
.news .photo{width:120px;height:84px;flex:none}
.news h3{font-size:13px;color:var(--brown);display:flex;justify-content:space-between;width:560px}
.news h3 time{font-size:9px;color:var(--muted);font-weight:400}
.news p{font-size:10.5px;margin-top:6px}
.menu li{list-style:none;border:1px solid var(--line);margin-bottom:6px;padding:5px 12px;font-size:11px;color:var(--brown);position:relative}
.menu li::after{content:"›";position:absolute;right:12px;color:var(--gold)}
.footer{left:0;top:2940px;width:1200px;height:200px;background:var(--brown);color:#e9e2d8}
.footer .brand-name{font-size:26px}
.fnav{right:40px;top:40px;display:flex;gap:18px;font-size:10px}
.fnav span::before{content:"› ";color:var(--gold)}
.finfo{left:48px;top:86px;font-size:10.5px;line-height:1.8}
.copyright{left:0;bottom:0;width:1200px;height:30px;background:var(--brown-dark);font-size:9px;line-height:30px;text-align:right;padding-right:40px}
</style>
</head>
<body>

<div class="abs topbar">tovaru（トヴァル）｜長野県の自然素材ナチュラル住宅ブランド</div>

<header class="abs masthead">
  <div class="abs brand"><span class="brand-mark"></span><span class="brand-name">Tovaru</span></div>
  <div class="abs cta" style="left:720px">
    <svg width="22" height="22" viewBox="0 0 24 24"><path d="M6 3l4 4-2 3c1 2 4 5 6 6l3-2 4 4-3 3C10 21 3 14 3 6z" fill="#4b4038"/></svg>
    <div><small>お電話でのお問い合わせ</small><b>0120-48-3917</b></div>
  </div>
  <div class="abs cta" style="left:945px">
    <svg width="22" height="18" viewBox="0 0 24 18"><rect x="1" y="1" width="22" height="16" fill="none" stroke="#4b4038" stroke-width="2"/><path d="M1 1l11 9 11-9" fill="none" stroke="#4b4038" stroke-width="2"/></svg>
    <div><small>24時間受付</small><span class="mail">メールフォームでのお問い合わせ</span></div>
  </div>
</header>

<nav class="abs nav">
  <a>ホーム</a><a>家づくり</a><a>施工事例</a><a>お問い合わせ</a><a>会社概要</a><a>会社情報</a>
</nav>

<div class="abs hero" role="img" aria-label="白い塗り壁と木製ドアの住宅外観写真"></div>
<div class="abs hero-caption">ローコスト住宅とナチュラルデザイン</div>

<section class="abs panel" style="left:40px;top:580px;width:740px;height:600px;padding:20px">
  <div class="head"><h2>BRAND CONCEPT</h2><span>ブランドコンセプト</span></div>
  <div style="display:flex;gap:22px">
    <div class="photo" role="img" aria-label="自然素材の内装写真" style="width:160px;height:240px;flex:none"></div>
    <div class="copy">
      <p>「自然が持つ美しさ」と「暮らす人の思い」を取り入れ『生活が楽しい住まい』を創ります。</p>
      <p>人々に永く愛されてきた天然素材を使用することで自然素材だけが持つ色や質感から確かな手触りと温もりを暮らす人に与え続けてくれます。新しいだけを追い過ぎず自然素材の持つ機能性を生かして自然の働きでしっかりと家を守る。</p>
      <p>それは流行に左右されない気品を保つ「素朴で美しい風合い」に仕上がります。</p>
      <p>住む人のライフスタイルや好みをしっかりとお聞かせいただいた上で土地を生かし隣地環境と調和のある設計を企画し、その人らしい家を一緒に考えていきます。</p>
      <p>それはその人がどんなふうに暮らしていきたいのかを一緒に考え、その地で永く暮らしていくイメージを膨らませ生活が楽しくなる様な空間を提案します。</p>
    </div>
  </div>
</section>

<section class="abs panel" style="left:800px;top:580px;width:360px;height:860px;padding:20px">
  <div class="head"><h2>BUILDING CASE</h2><span>施工事例</span></div>
  <div class="case-grid">
    <div><div class="photo sky" role="img" aria-label="施工事例の外観写真"></div>白い外壁の家</div>
    <div><div class="photo" role="img" aria-label="施工事例の外観写真"></div>木の玄関の家</div>
    <div><div class="photo" role="img" aria-label="施工事例の外観写真"></div>平屋の住まい</div>
    <div><div class="photo sky" role="img" aria-label="施工事例の外観写真"></div>二階建ての家</div>
    <div><div class="photo sky" role="img" aria-label="施工事例の外観写真"></div>塗り壁の家</div>
    <div><div class="photo" role="img" aria-label="施工事例の内観写真"></div>無垢床の家</div>
  </div>
  <a class="btn" style="margin-top:24px">施工事例一覧</a>
</section>

<section class="abs panel" style="left:40px;top:1200px;width:360px;height:250px;padding:20px">
  <div class="head"><h2>MAKING HOUSES</h2><span>ここに注目ください</span></div>
  <div class="copy"><p>ここに家づくりの考え方が入ります。ここに説明文が入ります。ここに説明文が入ります。ここに説明文が入ります。ここに説明文が入ります。ここに説明文が入ります。</p></div>
  <a class="btn" style="width:180px;margin-top:20px">詳しく見る</a>
</section>

<section class="abs panel" style="left:420px;top:1200px;width:360px;height:250px;padding:20px">
  <div class="head"><h2>CONTACT US</h2><span>お問い合わせ</span></div>
  <p style="font-size:10.5px">お問い合わせは下記まで。メールフォームからもお気軽にどうぞ。</p>
  <div class="cta" style="position:static;width:100%;margin-top:14px">
    <svg width="22" height="22" viewBox="0 0 24 24"><path d="M6 3l4 4-2 3c1 2 4 5 6 6l3-2 4 4-3 3C10 21 3 14 3 6z" fill="#4b4038"/></svg>
    <div><small>お電話でのお問い合わせ</small><b>0120-48-3917</b></div>
  </div>
  <div class="cta" style="position:static;width:100%;margin-top:10px">
    <svg width="22" height="18" viewBox="0 0 24 18"><rect x="1" y="1" width="22" height="16" fill="none" stroke="#4b4038" stroke-width="2"/><path d="M1 1l11 9 11-9" fill="none" stroke="#4b4038" stroke-width="2"/></svg>
    <div><small>24時間受付</small><span class="mail">メールフォームでのお問い合わせ</span></div>
  </div>
</section>

<section class="abs panel" style="left:40px;top:1480px;width:740px;height:900px;padding:20px">
  <div class="head"><h2>UPDATE INFORMATION</h2><span>最新情報</span></div>
  <ul class="news">
    <li><div class="photo" role="img" aria-label="ウッドデッキの写真"></div><div><h3>イベントによるウッドデッキ<time>2015.03.20</time></h3><p>ここに記事の概要が入ります。ここに記事の概要が入ります。ここに記事の概要が入ります。［続きを読む］</p></div></li>
    <li><div class="photo sky" role="img" aria-label="見学会の住宅写真"></div><div><h3>新築見学会を開催しました<time>2015.03.12</time></h3><p>ここに記事の概要が入ります。ここに記事の概要が入ります。ここに記事の概要が入ります。［続きを読む］</p></div></li>
    <li><div class="photo" role="img" aria-label="室内の写真"></div><div><h3>自然素材の内装　床と壁の素材選び<time>2015.02.28</time></h3><p>ここに記事の概要が入ります。ここに記事の概要が入ります。ここに記事の概要が入ります。［続きを読む］</p></div></li>
    <li><div class="photo sky" role="img" aria-label="外観の写真"></div><div><h3>ローコスト住宅と自然素材の家づくり<time>2015.02.15</time></h3><p>ここに記事の概要が入ります。ここに記事の概要が入ります。ここに記事の概要が入ります。［続きを読む］</p></div></li>
    <li><div class="photo" role="img" aria-label="住まいの写真"></div><div><h3>穏やかに暮らす家のための工夫<time>2015.02.01</time></h3><p>ここに記事の概要が入ります。ここに記事の概要が入ります。ここに記事の概要が入ります。［続きを読む］</p></div></li>
  </ul>
  <a class="btn" style="width:220px;margin:30px 0 0 auto">過去の記事を見る</a>
</section>

<section class="abs panel" style="left:800px;top:1480px;width:360px;height:400px;padding:20px">
  <div class="head"><h2>CONTENTS MENU</h2><span>メニュー</span></div>
  <ul class="menu">
    <li>ホーム</li><li>家づくり</li><li>施工事例</li><li>最新情報</li><li>お問い合わせ</li><li>会社概要</li><li>プライバシーポリシー</li>
  </ul>
</section>

<section class="abs panel" style="left:800px;top:1900px;width:360px;height:300px;padding:20px">
  <div class="head"><h2>COMPANY PROFILE</h2><span>会社概要</span></div>
  <div style="display:flex;gap:12px">
    <div class="photo sky" role="img" aria-label="事務所の外観写真" style="width:120px;height:90px;flex:none"></div>
    <p style="font-size:10px;line-height:1.7">ミナモ建築株式会社<br>〒396-0000<br>長野県緑川市中町1-2-3<br>TEL 0120-48-3917<br>info@tovaru.com</p>
  </div>
  <a class="btn" style="width:160px;margin-top:30px">詳しく見る</a>
</section>

<div class="abs" style="left:800px;top:2220px;width:360px;height:90px;border:1px solid var(--gold);background:var(--paper);display:flex;align-items:center;justify-content:center;font-family:'Noto Serif JP',serif;font-size:16px;color:var(--brown)">家づくりのご相談はこちら</div>

<section class="abs panel" style="left:40px;top:2400px;width:1120px;height:520px;padding:20px">
  <div class="head"><h2>CHECK SNS</h2><span>SNSのお知らせ</span></div>
  <div style="margin-left:120px;width:440px;height:420px;border:1px solid var(--line);background:var(--paper)">
    <div style="display:flex;gap:10px;align-items:center;padding:10px;border-bottom:1px solid var(--line)">
      <div class="photo" style="width:40px;height:40px"></div>
      <b style="font-size:11px;color:var(--brown)">tovaru トヴァル｜自然素材のナチュラル住宅</b>
    </div>
    <div style="padding:10px 14px">
      <b style="font-size:11px;color:var(--brown)">tovaru トヴァル｜自然素材のナチュラル住宅</b>
      <p style="font-size:10px;margin-top:6px">新築見学会を開催しました。ご来場ありがとうございました。次回の見学会のご案内は当ページでお知らせいたします。お気軽にご参加ください。</p>
      <div class="photo sky" role="img" aria-label="投稿された住宅外観写真" style="height:230px;margin-top:12px"></div>
    </div>
  </div>
</section>

<footer class="abs footer">
  <div class="abs brand" style="top:36px"><span class="brand-mark"></span><span class="brand-name">Tovaru</span></div>
  <div class="abs fnav"><span>ホーム</span><span>家づくり</span><span>施工事例</span><span>お問い合わせ</span><span>会社概要</span><span>プライバシーポリシー</span></div>
  <div class="abs finfo">ミナモ建築株式会社<br>〒396-0000　長野県緑川市中町1-2-3<br>TEL 0120-48-3917　MAIL info@tovaru.com</div>
  <div class="abs copyright">Copyright © TOVARU All Rights Reserved.</div>
</footer>

</body>
</html>
```